Cybersecurity company is looking for business card.

I need a business card design for our company, we are a cybersecurity company providing advance technology to protect agains any kind of malware. We need a fresh modern design it should communicate modern, technology and growth.

Target Market(s)

Business to business

Industry/Entity Type

Business

Contact Information for Business Card

Should have location, address, fax, mobile, phone, email and website.

Requirements
Must have
• Must follow company's logo color and style. Must have the company's log on its.

```html
<!DOCTYPE html>
<html lang="en">
<head>
<meta charset="utf-8">
<title>Veltrix Business Card</title>
<link href="https://fonts.googleapis.com/css2?family=Open+Sans:wght@400;600;800&display=swap" rel="stylesheet">
<style>
  :root {
    --backdrop: #6b3a2c;
    --card-white: #ffffff;
    --brand-red: #a30e10;
    --deep-red: #8e0c0e;
    --ink: #111111;
    --text-dark: #1d1d1d;
    --icon-grey: #5a5a5a;
    --label-white: #ffffff;
  }
  * { margin: 0; padding: 0; box-sizing: border-box; }
  html, body { width: 1200px; height: 900px; overflow: hidden; }
  body {
    background: var(--backdrop);
    font-family: "Open Sans", Arial, sans-serif;
    position: relative;
  }
  .sample-label {
    position: absolute;
    top: 168px; left: 0; width: 1200px;
    text-align: center;
    color: var(--label-white);
    font-size: 26px;
    font-family: Arial, "Open Sans", sans-serif;
    letter-spacing: 0.5px;
  }
  .card {
    position: absolute;
    top: 326px;
    width: 438px; height: 246px;
    overflow: hidden;
  }
  .card-front { left: 152px; background: var(--card-white); }
  .card-back { left: 610px; background: var(--brand-red); }

  .front-wordmark {
    position: absolute;
    right: 28px; top: 26px;
    font-size: 44px; font-weight: 800;
    color: var(--ink);
    line-height: 1;
    letter-spacing: 1px;
  }
  .front-rule {
    position: absolute;
    left: 12px; top: 78px;
    width: 403px; height: 1.5px;
    background: var(--deep-red);
  }
  .front-tab {
    position: absolute;
    left: 0; top: 71px;
    width: 12px; height: 16px;
    background: var(--brand-red);
  }
  .front-website {
    position: absolute;
    left: 43px; top: 65px;
    font-size: 9px;
    color: var(--brand-red);
  }
  .holder {
    position: absolute;
    right: 29px; top: 96px;
    text-align: right;
    color: var(--text-dark);
  }
  .holder-name { font-size: 12px; line-height: 1.3; }
  .holder-title { font-size: 8px; margin-top: 2px; }
  .contact-list {
    position: absolute;
    left: 23px; top: 156px;
    list-style: none;
  }
  .contact-list li {
    display: flex; align-items: center;
    height: 14px;
    font-size: 9.5px;
    color: var(--text-dark);
  }
  .contact-list svg { width: 11px; height: 11px; margin-right: 9px; flex: none; }
  .corner-peel { position: absolute; right: 0; bottom: 0; }

  .back-wordmark {
    position: absolute;
    left: 0; top: 82px; width: 438px;
    text-align: center;
    font-size: 84px; font-weight: 800;
    color: var(--ink);
    line-height: 1;
    letter-spacing: 3px;
  }
</style>
</head>
<body>
  <div class="sample-label">SAMPLE 1</div>

  <section class="card card-front">
    <div class="front-wordmark">veltrix</div>
    <div class="front-tab"></div>
    <div class="front-rule"></div>
    <div class="front-website">www.veltrix.com</div>
    <div class="holder">
      <div class="holder-name">Adam Rowe</div>
      <div class="holder-title">Director of Information Technology</div>
    </div>
    <ul class="contact-list">
      <li><svg viewBox="0 0 11 11"><rect x="0" y="0" width="11" height="11" rx="2" fill="var(--icon-grey)"/><rect x="3.5" y="1.8" width="4" height="7.4" rx="0.8" fill="#fff"/></svg>+971 50 555 0101</li>
      <li><svg viewBox="0 0 11 11"><rect x="0" y="0" width="11" height="11" rx="2" fill="var(--icon-grey)"/><path d="M3 2 L5 2 L5.6 4 L4.6 4.8 Q5.4 6.4 6.8 7.2 L7.6 6.2 L9.4 6.8 L9.4 8.8 Q5 9 2.5 4.4 Z" fill="#fff"/></svg>+971 04 555 0102</li>
      <li><svg viewBox="0 0 11 11"><rect x="0" y="0" width="11" height="11" rx="2" fill="var(--icon-grey)"/><rect x="2" y="4" width="7" height="5" fill="#fff"/><rect x="3" y="2" width="5" height="2" fill="#fff"/></svg>+971 04 555 0103</li>
      <li><svg viewBox="0 0 11 11"><rect x="0" y="0" width="11" height="11" rx="2" fill="var(--icon-grey)"/><rect x="2" y="3" width="7" height="5" fill="#fff"/><path d="M2 3 L5.5 6 L9 3" stroke="var(--icon-grey)" stroke-width="0.8" fill="none"/></svg>adam.rowe@veltrix.com</li>
      <li><svg viewBox="0 0 11 11"><rect x="0" y="0" width="11" height="11" rx="2" fill="var(--icon-grey)"/><path d="M5.5 1.8 A2.6 2.6 0 0 1 8.1 4.4 Q8.1 6.2 5.5 9.2 Q2.9 6.2 2.9 4.4 A2.6 2.6 0 0 1 5.5 1.8 Z" fill="#fff"/><circle cx="5.5" cy="4.4" r="1" fill="var(--icon-grey)"/></svg>Harbor Tech Park (HTP) Marina Road, Dubai - UAE</li>
    </ul>
    <svg class="corner-peel" width="64" height="66" viewBox="0 0 64 66">
      <path d="M4 0 L64 0 L2 66 L0 66 L0 4 Q0 0 4 0 Z" fill="var(--brand-red)"/>
    </svg>
  </section>

  <section class="card card-back">
    <div class="back-wordmark">veltrix</div>
  </section>
</body>
</html>
```